Need Letterhead Design & Matching Business Card

I have a logo that I love already. But the letterhead is less than appealing and boring. I'd like a design for my letterhead which I will match with business cards. Also, I'd like to have used fonts that are generally available, as my current letterhead uses a font named "SPACE" which nobody has unless they download it...so when a Word version is forwarded, it looks awful on the receiver's screed due to not having the font. That being said, modern is the look we like and are going for.

My business is "Halloran Brightmoor PC" - a law firm specializing in representing people who have suffered catastrophic injuries or death (plane, auto, train crashes etc.).

See attached letterhead, which has all of the pertinent information. My logo is also attached in various formats.

```html
<!DOCTYPE html>
<html lang="en">
<head>
<meta charset="utf-8">
<title>Halloran Brightmoor PC — Letterhead</title>
<link href="https://fonts.googleapis.com/css2?family=Montserrat:wght@400;500&display=swap" rel="stylesheet">
<style>
  :root {
    --ink: #111111;
    --paper: #ffffff;
    --muted: #4a4a4a;
    --rule: #1a1a1a;
    --footer-text: #e6e6e6;
  }
  * { margin: 0; padding: 0; box-sizing: border-box; }
  html, body { width: 849px; height: 1200px; overflow: hidden; background: var(--paper); }
  .letterhead {
    position: relative;
    width: 849px;
    height: 1200px;
    background: var(--paper);
    font-family: "Montserrat", Arial, sans-serif;
    color: var(--ink);
  }
  .brand {
    position: absolute;
    left: 16px;
    top: 20px;
    display: flex;
    align-items: center;
    gap: 12px;
  }
  .brand-square {
    width: 62px;
    height: 62px;
    background: var(--ink);
  }
  .brand-name {
    font-weight: 400;
    font-size: 27px;
    line-height: 1.02;
    letter-spacing: 2px;
    text-transform: uppercase;
    color: var(--ink);
  }
  .header-rule {
    position: absolute;
    left: 16px;
    right: 16px;
    top: 112px;
    height: 2px;
    background: var(--rule);
  }
  .contact {
    position: absolute;
    right: 18px;
    top: 42px;
    text-align: right;
    font-size: 11.5px;
    line-height: 20px;
    letter-spacing: 1.2px;
    text-transform: uppercase;
    color: var(--ink);
  }
  .contact .title { color: var(--muted); }
  .footer {
    position: absolute;
    left: 0;
    right: 0;
    bottom: 0;
    height: 116px;
    background: var(--ink);
    color: var(--footer-text);
    display: flex;
    justify-content: space-between;
    align-items: flex-end;
    padding: 0 28px 26px 62px;
    font-size: 11px;
    letter-spacing: 1.1px;
    text-transform: uppercase;
  }
  .footer-address { line-height: 16px; }
  .footer-web { line-height: 16px; padding-bottom: 10px; }
</style>
</head>
<body>
  <main class="letterhead">
    <header>
      <div class="brand">
        <div class="brand-square"></div>
        <div class="brand-name">Halloran<br>Brightmoor PC</div>
      </div>
      <div class="contact">
        <div>M. Dorian Castell, Esq. <span class="title">| President</span></div>
        <div>dorian@halloranbrightmoor.com</div>
        <div>Tel. (310) 555-0147</div>
      </div>
      <div class="header-rule"></div>
    </header>

    <footer class="footer">
      <div class="footer-address">
        <div>Halloran Brightmoor PC</div>
        <div>4420 Larchmont Ave. | Suite 800</div>
        <div>Westbrook, CA 90299</div>
      </div>
      <div class="footer-web">www.halloranbrightmoor.com</div>
    </footer>
  </main>
</body>
</html>
```